You Be The Rock Star Ad Campaign

Series of 3 ads for Marketing Campaign, able to be interchangeable for different featured products with the ability to fit 1 to 2 products per ad.
Tagline: You Be The Rock Star, We'll Supply The Instruments.
Keep with corporate colors: Teal 323C and Cool Grey 4, Orange 21 for some concepts.
Subheading for body copy withing ad should read Innovative Technology Engineered to Perform

Target Market(s)

Roof contractors

Industry/Entity Type

Roofing

Font styles to use
Serif
Sans Serif

Requirements
Must have
• Vextrona logo (provided). Use current branding, see www.vextrona.us for examples
• Tagline: You Be The Rock Star, We'll Supply The Instruments
• Call out: Innovative Technology Engineered to Perform
• Include the website: www.vextrona.us
Nice to have
• Rock concert or rock band, branded instruments.
Should not have
• No residential buildings images.

```html
<!DOCTYPE html>
<html lang="en">
<head>
<meta charset="utf-8">
<title>Vextrona – You Be The Rockstar</title>
<link rel="stylesheet" href="https://fonts.googleapis.com/css2?family=Lato:wght@300;400;700;900&display=swap">
<style>
  :root {
    --teal: #2e6b60;
    --teal-deep: #1f5048;
    --teal-light: #4f8c80;
    --ink: #222222;
    --grey-page: #a6a6a8;
    --white: #ffffff;
    --product-grey: #dfe3e6;
    --product-blue: #2a3f8f;
  }
  * { box-sizing: border-box; margin: 0; padding: 0; }
  html, body {
    width: 1200px; height: 864px; overflow: hidden;
    background: var(--grey-page);
    font-family: "Lato", sans-serif;
  }
  .ad {
    position: absolute; left: 311px; top: 24px;
    width: 578px; height: 816px;
    background: var(--white);
    box-shadow: 10px 12px 14px rgba(0,0,0,0.25);
    overflow: hidden;
  }
  .hero {
    position: absolute; left: 0; top: 0; width: 578px; height: 489px;
    background:
      radial-gradient(ellipse at 70% 35%, var(--teal-light) 0%, transparent 60%),
      linear-gradient(180deg, var(--teal) 0%, var(--teal-deep) 100%);
  }
  .headline { position: absolute; left: 56px; color: var(--white); font-weight: 900; line-height: 1; letter-spacing: -0.5px; }
  .headline--lead { top: 56px; font-size: 42px; }
  .headline--star { top: 98px; font-size: 86px; letter-spacing: -1.5px; }
  .headline--supply { top: 192px; font-size: 44px; line-height: 41px; }
  .callout {
    position: absolute; left: 99px; top: 355px;
    color: var(--white); font-weight: 700; font-size: 26px; line-height: 29px;
  }
  .products-rolls {
    position: absolute; left: 297px; top: 434px; width: 218px; height: 158px;
    background: linear-gradient(90deg, var(--product-grey) 0%, var(--product-blue) 30%, var(--product-grey) 45%, #f1f2f3 75%, var(--product-blue) 100%);
    border-radius: 4px;
  }
  .products-pails {
    position: absolute; left: 66px; top: 513px; width: 217px; height: 74px;
    background: linear-gradient(90deg, #e9ecf0 0%, #9a9ca0 25%, #e9ecf0 45%, var(--product-blue) 60%, #e9ecf0 100%);
    border-radius: 4px;
  }
  .copy {
    position: absolute; left: 55px; top: 615px; width: 468px;
    display: grid; grid-template-columns: 1fr 1fr; column-gap: 12px;
    font-size: 10px; line-height: 12.6px; color: var(--ink); font-weight: 400;
  }
  .copy__title { font-weight: 900; font-size: 10.5px; margin-bottom: 12px; }
  .copy p { text-align: justify; }
  .brand {
    position: absolute; left: 55px; top: 726px;
    display: flex; align-items: center; gap: 8px;
  }
  .brand__badge { width: 36px; height: 34px; background: #c8c9cb; border: 1px solid #9c9da0; }
  .brand__name { font-weight: 900; font-size: 24px; color: var(--teal); letter-spacing: 0.5px; }
  .cta { position: absolute; right: 55px; top: 741px; text-align: left; }
  .cta__label { font-size: 12px; font-weight: 400; color: #333; letter-spacing: 0.3px; }
  .cta__url { font-size: 15px; font-weight: 900; color: var(--teal); }
</style>
</head>
<body>
  <article class="ad">
    <section class="hero" role="img" aria-label="Rock band performing on a smoky stage with guitars and drums, tinted teal">
    </section>
    <h1 class="headline headline--lead">YOU BE THE</h1>
    <p class="headline headline--star">ROCKSTAR</p>
    <p class="headline headline--supply">WE’LL SUPPLY<br>THE INSTRUMENTS</p>
    <h2 class="callout">INNOVATIVE<br>TECHNOLOGY<br>ENGINEERED<br>TO PERFORM</h2>

    <div class="products-rolls" role="img" aria-label="Rolls and boxes of reflective roofing membrane"></div>
    <div class="products-pails" role="img" aria-label="Pails of elastomeric roof coating"></div>

    <section class="copy">
      <div>
        <h3 class="copy__title">KOOL ROOF SOLUTIONS</h3>
        <p>Specially formulated in our laboratories using state-of-the-art technologies, and manufactured with the highest quality ingredients, these modified bitumen</p>
      </div>
      <p>membranes and elastometric coatings are designed to reflect the sun’s rays away from your building, keeping interior temperatures comfortable and adding up to significant savings on energy bills over time.</p>
    </section>

    <div class="brand">
      <span class="brand__badge" aria-hidden="true"></span>
      <span class="brand__name">VEXTRONA</span>
    </div>

    <div class="cta">
      <p class="cta__label">LEARN MORE</p>
      <p class="cta__url">www.vextrona.us</p>
    </div>
  </article>
</body>
</html>
```